Ledgerwise 540 for Tavlo

We are looking to design a page for the mobile app. The app is intended for financial professionals and is based on a successful desktop application. The existing design will serve as a very rough guideline, but we are open to hearing ideas.
Uploaded file #1 contains a screenshot of the existing design. The workflow is as follows:
The user picks a portfolio from the Dropdown below portfolio.
The user picks a Loss Threshold, which will dictate what gets onto the bubble chart below.
Once the bubble on the chart is clicked, a text box pops up with the description of the particular crisis that the bubble represents.
Once the bubble is clicked, the right hand side bar charts are populated with moves relevant to this scenario.
The left hand pane contains two text boxes. The lower one is particularly important, because the user is able to remove scenarios or add scenarios (screen #2). Removing scenarios is simple.
Adding scenarios brings up a wizard (screen #3). It also needs to be designed consistently with the front page of the app. The wizard has different clickable categories going down the column on the left and in a row on the top. The user can pick some or all of these categories.

Notes: The app should be designed for landscape mode only. The key to keep in mind is how the user will select bubbles on the chart. Right now, it is quite easy, but with the touchscreen it may be more complicated, so please keep that in mind when designing the chart (it should still be some version of the similar chart).
*As a first pass, please submit your idea of the concept (layout/colors/buttons) without the detailed design. We will choose 1-3 concepts and then the detailed work will take place with a much higher chance of a payout.
Updates

Thank you for the first two sketches. The second one by bertrand appears to be a bit more mobile app oriented, though we are still considering both and waiting for other submissions. One request, could you rework the sketches to include a bit more of dark blue as a background?  \

Bertrand, I think that the bubbles are too small and they are missing some volume effects. Could you make them a bit more prominent (and pick some form of dark blue background) and change the color to see if they will stand out better?
 

Industry/Entity Type

Financial

Requirements
Must have
• The general outline for the bubble chart must be retained. But the actual execution may differ significantly. We are open to seeing different ideas.
The winning design will also get a contract to design the rest of the application (2 more screens), which will be worth the same as the original design.

```html
<!DOCTYPE html>
<html lang="en">
<head>
<meta charset="utf-8">
<title>Ledgerwise 540 – Scenario Chart</title>
<link rel="stylesheet" href="https://fonts.googleapis.com/css2?family=Arimo:wght@400;700&display=swap">
<style>
:root{
  --status:#0b0b0c;
  --toolbar:#24272c;
  --app-bg:#2e3136;
  --panel:#23262a;
  --plot:#2a2d31;
  --grid:#3f4348;
  --axis-text:#8c9097;
  --accent:#2fa8e8;
  --accent-dark:#1673b0;
  --sidebar:#e6e6e7;
  --chart-box:#1f2226;
  --track:#0f1113;
  --neg:#e8305a;
  --white:#ffffff;
  --ink:#1d1f22;
}
*{box-sizing:border-box;margin:0;padding:0}
html,body{width:1200px;height:901px;overflow:hidden;background:var(--app-bg);font-family:"Arimo",Arial,sans-serif}
.screen{position:relative;width:1200px;height:901px;background:var(--app-bg)}
.status-bar{position:absolute;left:0;top:0;width:1200px;height:24px;background:var(--status);color:var(--white);font-size:15px}
.status-bar .device{position:absolute;left:6px;top:3px}
.status-bar .time{position:absolute;left:0;right:0;top:3px;text-align:center;font-weight:700}
.status-bar .battery{position:absolute;right:8px;top:6px;width:24px;height:12px;border:1.5px solid #fff;border-radius:2px;padding:1px}
.status-bar .battery i{display:block;height:100%;background:#fff}
.toolbar{position:absolute;left:0;top:24px;width:1200px;height:52px;background:linear-gradient(#2f3338,#1d2024);border-bottom:1px solid #111}
.brand{position:absolute;left:15px;top:16px;color:var(--accent);font-weight:700;font-size:15px}
.select{position:absolute;top:11px;height:26px;background:#17191c;border:1px solid #3a3e44;border-radius:3px;color:var(--accent);font-size:15px;padding:4px 7px}
.select .caret{position:absolute;right:0;top:0;width:22px;height:24px;border-left:1px solid #3a3e44;background:#25282d}
.select .caret::after{content:"";position:absolute;left:6px;top:9px;border:5px solid transparent;border-top:7px solid var(--accent)}
.menu-btn{position:absolute;left:1152px;top:17px;width:22px}
.menu-btn i{display:block;height:3px;background:var(--accent);margin-bottom:4px;border-radius:1px}
.side-tab{position:absolute;left:0;top:85px;width:25px;height:800px;background:var(--sidebar)}
.play{position:absolute;width:16px;height:16px;border-radius:50%;background:#8d9096}
.play::after{content:"";position:absolute;left:6px;top:4px;border:4px solid transparent;border-left:6px solid #e6e6e7}
.chart-panel{position:absolute;left:43px;top:118px;width:824px;height:735px;background:var(--panel);border-radius:4px}
.graph-title{position:absolute;left:0;width:810px;top:22px;text-align:center;color:#e8e9ea;font-size:14px}
.chart-svg{position:absolute;left:0;top:0}
.tooltip{position:absolute;left:193px;top:423px;width:272px;height:115px;background:#15171a;border:1px solid #3b3f44;border-radius:4px;color:#fff;padding:7px 14px}
.tooltip::after{content:"";position:absolute;left:133px;bottom:-11px;border:10px solid transparent;border-top:10px solid #15171a;border-bottom:0}
.tooltip h3{font-size:19px;font-weight:700;padding-bottom:8px;border-bottom:1px solid #3b3f44;margin:0 -14px 11px;padding-left:14px}
.tooltip p{font-size:15px;line-height:19px}
.dropdown{position:absolute;left:60px;top:86px;width:218px;height:152px;background:#2c2f34;border:1px solid #4a4e55;border-radius:4px;padding:4px}
.dropdown::before{content:"";position:absolute;left:100px;top:-12px;border:10px solid transparent;border-bottom:12px solid #4a4e55;border-top:0}
.dropdown ul{list-style:none;background:var(--white);height:142px;border-radius:2px;overflow:hidden;position:relative}
.dropdown li{height:29px;border-bottom:1px solid #d6d6d6;font-size:13px;font-weight:700;color:var(--ink);padding:8px 6px}
.dropdown .scroll{position:absolute;right:3px;top:4px;width:3px;height:122px;background:#999;border-radius:2px}
.sidebar{position:absolute;left:883px;top:85px;width:309px;height:800px;background:var(--sidebar);border-radius:3px}
.sidebar-title{position:absolute;top:9px;width:100%;text-align:center;font-weight:700;font-size:14px;color:var(--ink)}
.bar-title{position:absolute;left:20px;width:275px;text-align:center;font-size:14px;color:#2b2d30}
.bar-box{position:absolute;left:20px;width:275px;background:var(--chart-box);border-radius:3px}
.bar-row{position:absolute;left:8px;width:258px;height:20px;color:#e3e4e6;font-size:7px}
.bar-row .name{position:absolute;left:1px;top:0}
.bar-row .val{position:absolute;right:0;top:0}
.bar-row .track{position:absolute;left:0;top:9px;width:258px;height:9px;background:var(--track)}
.bar-row .fill{position:absolute;top:0;height:9px}
.pos .fill{left:0;background:linear-gradient(#4cc0f5,#1c86cc)}
.neg .fill{right:0;background:linear-gradient(#ff5a7c,#d91f48)}
.axis-labels{position:absolute;left:20px;width:275px;display:flex;justify-content:space-between;font-size:10px;color:#2b2d30}
</style>
</head>
<body>
<div class="screen">
  <div class="status-bar">
    <span class="device">Tavlo</span>
    <span class="time">4:21 PM</span>
    <span class="battery"><i></i></span>
  </div>

  <header class="toolbar">
    <span class="brand">Ledgerwise 540</span>
    <div class="select" style="left:95px;width:151px">Portfolio Date<span class="caret"></span></div>
    <div class="select" style="left:295px;width:151px">Portfolio<span class="caret"></span></div>
    <div class="select" style="left:494px;width:98px">Currency<span class="caret"></span></div>
    <div class="select" style="left:640px;width:152px">Weight Type<span class="caret"></span></div>
    <div class="select" style="left:835px;width:152px">Model<span class="caret"></span></div>
    <div class="select" style="left:1028px;width:76px">Loss<span class="caret"></span></div>
    <div class="menu-btn"><i></i><i></i><i></i></div>
  </header>

  <aside class="side-tab"><span class="play" style="left:4px;top:9px"></span></aside>

  <section class="chart-panel">
    <div class="graph-title">Graph Title</div>
    <svg class="chart-svg" width="824" height="735" viewBox="43 118 824 735" xmlns="http://www.w3.org/2000/svg">
      <defs>
        <radialGradient id="bubble" cx="40%" cy="35%" r="65%">
          <stop offset="0" stop-color="#aee6ff"/>
          <stop offset="0.35" stop-color="#3aaef0"/>
          <stop offset="1" stop-color="#0f5e9e"/>
        </radialGradient>
        <radialGradient id="bubble-sel" cx="40%" cy="35%" r="65%">
          <stop offset="0" stop-color="#ffffff"/>
          <stop offset="0.5" stop-color="#c8ccd2"/>
          <stop offset="1" stop-color="#7c828b"/>
        </radialGradient>
      </defs>
      <rect x="120" y="174" width="697" height="606" fill="var(--plot)" stroke="#55595f"/>
      <g stroke="var(--grid)" stroke-width="1">
        <line x1="163.5" y1="174" x2="163.5" y2="780"/><line x1="207" y1="174" x2="207" y2="780"/>
        <line x1="250.5" y1="174" x2="250.5" y2="780"/><line x1="294" y1="174" x2="294" y2="780"/>
        <line x1="337.5" y1="174" x2="337.5" y2="780"/><line x1="381" y1="174" x2="381" y2="780"/>
        <line x1="424.5" y1="174" x2="424.5" y2="780"/><line x1="468" y1="174" x2="468" y2="780"/>
        <line x1="511.5" y1="174" x2="511.5" y2="780"/><line x1="555" y1="174" x2="555" y2="780"/>
        <line x1="598.5" y1="174" x2="598.5" y2="780"/><line x1="642" y1="174" x2="642" y2="780"/>
        <line x1="685.5" y1="174" x2="685.5" y2="780"/><line x1="729" y1="174" x2="729" y2="780"/>
        <line x1="772.5" y1="174" x2="772.5" y2="780"/>
        <line x1="120" y1="213" x2="817" y2="213"/><line x1="120" y1="251" x2="817" y2="251"/>
        <line x1="120" y1="289" x2="817" y2="289"/><line x1="120" y1="327" x2="817" y2="327"/>
        <line x1="120" y1="364" x2="817" y2="364"/><line x1="120" y1="402" x2="817" y2="402"/>
        <line x1="120" y1="440" x2="817" y2="440"/><line x1="120" y1="478" x2="817" y2="478"/>
        <line x1="120" y1="516" x2="817" y2="516"/><line x1="120" y1="553" x2="817" y2="553"/>
        <line x1="120" y1="591" x2="817" y2="591"/><line x1="120" y1="629" x2="817" y2="629"/>
        <line x1="120" y1="667" x2="817" y2="667"/><line x1="120" y1="705" x2="817" y2="705"/>
        <line x1="120" y1="742" x2="817" y2="742"/>
      </g>
      <g fill="var(--axis-text)" font-size="11" font-family="Arimo, sans-serif" text-anchor="end">
        <text x="109" y="255">-10</text><text x="109" y="293">-11</text><text x="109" y="331">-12</text>
        <text x="109" y="368">-13</text><text x="109" y="406">-14</text><text x="109" y="444">-15</text>
        <text x="109" y="482">-16</text><text x="109" y="520">-17</text><text x="109" y="557">-18</text>
        <text x="109" y="595">-19</text><text x="109" y="633">-20</text><text x="109" y="671">-21</text>
        <text x="109" y="709">-22</text><text x="109" y="746">-23</text><text x="109" y="784">-24</text>
      </g>
      <g fill="var(--axis-text)" font-size="11" font-family="Arimo, sans-serif" text-anchor="middle">
        <text x="122" y="803">-24</text><text x="157" y="803">-23</text><text x="201" y="803">-22</text>
        <text x="245" y="803">-21</text><text x="288" y="803">-20</text><text x="334" y="803">-19</text>
        <text x="375" y="803">-18</text><text x="419" y="803">-17</text><text x="465" y="803">-16</text>
        <text x="508" y="803">-15</text><text x="551" y="803">-14</text><text x="594" y="803">-13</text>
        <text x="638" y="803">-12</text><text x="683" y="803">-11</text><text x="727" y="803">-10</text>
        <text x="770" y="803">-9</text><text x="814" y="803">-8</text>
        <text x="454" y="829" font-size="14">Loss</text>
        <text x="72" y="485" font-size="14" transform="rotate(-90 72 485)">Correlation Suprise</text>
      </g>
      <circle cx="685" cy="291" r="12" fill="url(#bubble)"/>
      <circle cx="700" cy="275" r="12" fill="url(#bubble)"/>
      <circle cx="226" cy="730" r="12" fill="url(#bubble)"/>
      <circle cx="337" cy="590" r="22" fill="#0f1a26" stroke="#2b6fa3" stroke-width="2"/>
      <circle cx="337" cy="590" r="17" fill="none" stroke="var(--accent)" stroke-width="3"/>
      <circle cx="337" cy="590" r="12" fill="url(#bubble-sel)"/>
    </svg>
    <div class="tooltip" style="left:150px;top:305px">
      <h3>Name: Stagflation Severe</h3>
      <p>LOSS: -18.82</p>
      <p>Plausibility: 0.00</p>
      <p>Correlation Surprise: -18.82</p>
    </div>
  </section>

  <div class="dropdown">
    <ul>
      <li>Label</li><li>Label</li><li>Label</li><li>Label</li><li>Label</li>
      <span class="scroll"></span>
    </ul>
  </div>

  <aside class="sidebar">
    <div class="sidebar-title">Left Sidebar Title</div>
    <span class="play" style="left:290px;top:9px"></span>

    <div class="bar-title" style="top:59px">Asset Contribution 10 Highest</div>
    <div class="bar-box" style="top:78px;height:300px">
      <div class="bar-row pos" style="top:9px"><span class="name">HXB 6.505 02/12/67</span><span class="val">0.083</span><span class="track"><span class="fill" style="width:231px"></span></span></div>
      <div class="bar-row pos" style="top:38px"><span class="name">TVX 6 02/15/67</span><span class="val">0.071</span><span class="track"><span class="fill" style="width:196px"></span></span></div>
      <div class="bar-row pos" style="top:67px"><span class="name">FRLB 6 .5 04/15/37</span><span class="val">0.038</span><span class="track"><span class="fill" style="width:117px"></span></span></div>
      <div class="bar-row pos" style="top:96px"><span class="name">GQ 5 .5 12/31/49</span><span class="val">0.017</span><span class="track"><span class="fill" style="width:80px"></span></span></div>
      <div class="bar-row pos" style="top:125px"><span class="name">TDRCN 7 .876 01/15/19</span><span class="val">0.016</span><span class="track"><span class="fill" style="width:73px"></span></span></div>
      <div class="bar-row pos" style="top:154px"><span class="name">UAR Float 07/02/14</span><span class="val">0.009</span><span class="track"><span class="fill" style="width:47px"></span></span></div>
      <div class="bar-row pos" style="top:183px"><span class="name">WQM 7.506 05/29/49</span><span class="val">0.009</span><span class="track"><span class="fill" style="width:47px"></span></span></div>
      <div class="bar-row pos" style="top:212px"><span class="name">MERIDO 12.5 01/15/18</span><span class="val">0.002</span><span class="track"><span class="fill" style="width:15px"></span></span></div>
      <div class="bar-row pos" style="top:241px"><span class="name">BIRX 10 .25 10/01/15</span><span class="val">0.002</span><span class="track"><span class="fill" style="width:12px"></span></span></div>
      <div class="bar-row pos" style="top:270px"><span class="name">YQC 10 .25 02/15/16</span><span class="val">0.001</span><span class="track"><span class="fill" style="width:9px"></span></span></div>
    </div>
    <div class="axis-labels" style="top:389px"><span>0.00</span><span>0.02</span><span>0.04</span><span>0.06</span><span>0.08</span><span>0.10</span></div>

    <div class="bar-title" style="top:429px">Asset Contribution 10 Lowest</div>
    <div class="bar-box" style="top:448px;height:305px">
      <div class="bar-row neg" style="top:9px"><span class="name">WQ 7 .375 03/15/32</span><span class="val">-0.320</span><span class="track"><span class="fill" style="width:8px"></span></span></div>
      <div class="bar-row neg" style="top:38px"><span class="name">TURKEY 7 06/05/20</span><span class="val">-0.322</span><span class="track"><span class="fill" style="width:14px"></span></span></div>
      <div class="bar-row neg" style="top:67px"><span class="name">TII 0 .125 01/122</span><span class="val">-0.343</span><span class="track"><span class="fill" style="width:14px"></span></span></div>
      <div class="bar-row neg" style="top:96px"><span class="name">TQ 3 .125 02/15/43</span><span class="val">-0.352</span><span class="track"><span class="fill" style="width:46px"></span></span></div>
      <div class="bar-row neg" style="top:125px"><span class="name">INDON 5 .875 03/13/20</span><span class="val">-0.354</span><span class="track"><span class="fill" style="width:46px"></span></span></div>
      <div class="bar-row neg" style="top:154px"><span class="name">WAVU 2005-AR6 X</span><span class="val">-0.360</span><span class="track"><span class="fill" style="width:72px"></span></span></div>
      <div class="bar-row neg" style="top:183px"><span class="name">RUSSIA 4 .5 04/01/22</span><span class="val">-0.370</span><span class="track"><span class="fill" style="width:80px"></span></span></div>
      <div class="bar-row neg" style="top:212px"><span class="name">TII 3 .875 04/15/30</span><span class="val">-0.577</span><span class="track"><span class="fill" style="width:116px"></span></span></div>
      <div class="bar-row neg" style="top:241px"><span class="name">AXOSA 8.6 12/15/30</span><span class="val">-0.900</span><span class="track"><span class="fill" style="width:194px"></span></span></div>
      <div class="bar-row neg" style="top:270px"><span class="name">SP 0 08/15/41</span><span class="val">-1.975</span><span class="track"><span class="fill" style="width:230px"></span></span></div>
    </div>
    <div class="axis-labels" style="top:759px"><span>-2.5</span><span>-2.0</span><span>-1.5</span><span>-1.0</span><span>-0.5</span><span>0.0</span></div>
  </aside>
</div>
</body>
</html>
```